Design some Business Cards

Thank you so much for viewing my contest ! Please be creative
I need some business cards with a cool design, simple and professional.
Below i will add 2 Logos. I want a matte black Background Entry, and a white background entry both front and back. PLEASE KEEP ORIGINAL LOGO COLORS
Please add to the back of the card
Service/Repair/Installations
Duct cleaning services
Miami Dade/Broward County
Call now for a free quote
Special Duct Cleaning Prices
I will need to include contact info for example:
social
Email
Phone Number
Thank you any questions feel free to contact me.!
I appreciate any creative work!

```html
<!DOCTYPE html>
<html lang="en">
<head>
<meta charset="utf-8">
<title>Cool Current Air Conditioning – Business Cards</title>
<link href="https://fonts.googleapis.com/css2?family=Montserrat:wght@400;600;800&family=Open+Sans:wght@400;600&display=swap" rel="stylesheet">
<style>
  :root {
    --bg: #7a5c3c;
    --card-black: #0d0d0e;
    --brand-blue: #3f9cc0;
    --brand-red: #d8333b;
    --ink-dark: #16282f;
    --rule-white: #f2f2f2;
  }
  * { margin: 0; padding: 0; box-sizing: border-box; }
  html, body { width: 1200px; height: 803px; overflow: hidden; }
  body {
    background: var(--bg);
    position: relative;
    font-family: "Open Sans", sans-serif;
  }
  .card {
    position: absolute;
    top: 253px;
    width: 520px;
    height: 297px;
    background: var(--card-black);
    overflow: hidden;
  }
  .card--front { left: 60px; }
  .card--back { left: 620px; }

  /* Front */
  .front__rule {
    position: absolute;
    left: 0; right: 0; bottom: 18px;
    height: 5px;
    background: var(--brand-blue);
  }
  .brand {
    position: absolute;
    left: 0; right: 0; top: 100px;
    display: flex;
    flex-direction: column;
    align-items: center;
  }
  .brand__name {
    font-family: "Montserrat", sans-serif;
    font-weight: 800;
    font-size: 40px;
    letter-spacing: 1px;
    color: var(--brand-blue);
  }
  .brand__tagline {
    margin-top: 10px;
    font-family: "Montserrat", sans-serif;
    font-weight: 600;
    font-size: 11px;
    letter-spacing: 7px;
    color: var(--brand-red);
    text-transform: uppercase;
  }

  /* Back */
  .back__band {
    position: absolute;
    left: 0; right: 0; top: 0;
    height: 104px;
  }
  .back__accent {
    position: absolute;
    left: 0; right: 0; top: 14px;
    height: 3px;
    background: var(--brand-blue);
  }
  .holder {
    position: absolute;
    left: 0; right: 0; top: 44px;
    text-align: center;
  }
  .holder__name {
    font-family: "Montserrat", sans-serif;
    font-weight: 600;
    font-size: 22px;
    letter-spacing: 1px;
    color: var(--brand-red);
  }
  .holder__title {
    font-size: 11px;
    color: var(--brand-red);
    margin-top: 2px;
  }
  .contacts {
    position: absolute;
    left: 0; right: 0; top: 104px; bottom: 0;
    display: flex;
    gap: 9px;
  }
  .contact {
    flex: 1;
    background: var(--brand-blue);
    display: flex;
    flex-direction: column;
    align-items: center;
    justify-content: center;
    gap: 10px;
    color: var(--ink-dark);
    font-size: 12px;
  }
  .contact svg { width: 18px; height: 18px; fill: var(--ink-dark); }
  .contact--split { gap: 12px; }
  .contact__item {
    display: flex;
    flex-direction: column;
    align-items: center;
    gap: 6px;
  }
  .contact__divider {
    width: 70%;
    height: 2px;
    background: var(--rule-white);
  }
</style>
</head>
<body>

  <section class="card card--front" aria-label="Card front">
    <div class="brand">
      <span class="brand__name">COOL CURRENT</span>
      <span class="brand__tagline">Air Conditioning</span>
    </div>
    <div class="front__rule"></div>
  </section>

  <section class="card card--back" aria-label="Card back">
    <div class="back__band">
      <div class="back__accent"></div>
      <div class="holder">
        <div class="holder__name">YOUR NAME</div>
        <div class="holder__title">Title</div>
      </div>
    </div>
    <div class="contacts">
      <div class="contact">
        <svg viewBox="0 0 24 24" aria-hidden="true"><path d="M6.6 10.8a15.1 15.1 0 0 0 6.6 6.6l2.2-2.2c.3-.3.7-.4 1-.2 1.1.4 2.3.6 3.6.6.6 0 1 .4 1 1V20c0 .6-.4 1-1 1A17 17 0 0 1 3 4c0-.6.4-1 1-1h3.5c.6 0 1 .4 1 1 0 1.3.2 2.5.6 3.6.1.3 0 .7-.2 1z"/></svg>
        <span>Phone Number</span>
      </div>
      <div class="contact">
        <svg viewBox="0 0 24 24" aria-hidden="true"><path d="M12 2a7 7 0 0 0-7 7c0 5.2 7 13 7 13s7-7.8 7-13a7 7 0 0 0-7-7zm0 9.5A2.5 2.5 0 1 1 12 6.5a2.5 2.5 0 0 1 0 5z"/></svg>
        <span>location</span>
      </div>
      <div class="contact contact--split">
        <div class="contact__item">
          <svg viewBox="0 0 24 24" aria-hidden="true"><path d="M3 5h18v14H3zm2 2v.5l7 4.5 7-4.5V7zm0 2.9V17h14V9.9l-7 4.5z"/></svg>
          <span>Your mail</span>
        </div>
        <div class="contact__divider"></div>
        <div class="contact__item">
          <svg viewBox="0 0 24 24" aria-hidden="true"><path d="M4 4h16v12H8l-4 4z"/></svg>
          <span>social</span>
        </div>
      </div>
    </div>
  </section>

</body>
</html>
```